Inspirational Card with Words of Wisdom to Give to Kids

I run basketball camps and give inspirational messages to elementary schools and high schools (www.pastthebrightline.net).

I would like to create a card that has some inspirational thoughts and words of wisdom on it that I can give away...and that students and athletes will keep in their wallet as a reminder of things I've taught them.

I want it to be clean and classy, while not looking too child-like or business-like, as I'd like to be able to give it out to kids, teenagers, and young adults.

The card will be the size of a regular business card and will be double-sided. I would like to use black, orange, gray, and white as the primary colors, with white or gray likely being the background color.
Updates

You're welcome to leave off the title "Wisdom for Life" if desired and just use "The Triple Crown of Success" on the front of the card.

Thanks.

If you choose to leave off the poem, which you're welcome to do, please make one minor addition to the 5-point creed:

Add the words "God and" to "Honour others in everything you say and do" so it becomes:

"Honour God and others in everything you say and do."

Target Market(s)

Children, Teenagers, and Young Adults

Industry/Entity Type

Business

Requirements
Must have
• All the content, although the poem could be removed if necessary.
Should not have
• Nothing basketball-specific, as I want to be able to give it out to any child or teenager.

```html
<!DOCTYPE html>
<html lang="en">
<head>
<meta charset="UTF-8">
<title>5-Point Creed Card</title>
<link href="https://fonts.googleapis.com/css2?family=Crimson+Pro:ital,wght@0,400;0,500;1,400&display=swap" rel="stylesheet">
<style>
  :root {
    --card-gray: #e6e5e3;
    --ink: #161616;
    --accent-orange: #e07a1f;
  }
  html, body {
    margin: 0;
    padding: 0;
    width: 1200px;
    height: 800px;
    overflow: hidden;
    background: var(--card-gray);
  }
  .card {
    position: relative;
    width: 1200px;
    height: 800px;
    background: var(--card-gray);
    font-family: "Crimson Pro", Georgia, serif;
    font-variant-numeric: oldstyle-nums;
    color: var(--ink);
  }
  .creed-title {
    position: absolute;
    left: 22px;
    top: 56px;
    margin: 0;
    font-size: 35px;
    font-weight: 500;
    color: var(--accent-orange);
    line-height: 1;
  }
  .creed-list {
    position: absolute;
    left: 20px;
    top: 131px;
    margin: 0;
    padding: 0;
    list-style: none;
    font-size: 27px;
    line-height: 34px;
  }
  .pledge {
    position: absolute;
    left: 314px;
    top: 400px;
    width: 860px;
    font-size: 26px;
    line-height: 34px;
  }
  .pledge-heading {
    margin: 0;
    font-weight: 500;
    font-size: 26px;
    color: var(--accent-orange);
  }
  .pledge-text {
    margin: 0;
    white-space: nowrap;
  }
  .sign-field {
    position: absolute;
    text-align: center;
    font-size: 27px;
  }
  .sign-line {
    border-bottom: 2px solid var(--ink);
    margin-bottom: 6px;
  }
  .sign-signature { left: 526px; top: 516px; width: 330px; }
  .sign-date { left: 520px; top: 610px; width: 328px; }
  .motto {
    position: absolute;
    left: 0;
    top: 718px;
    width: 1200px;
    text-align: center;
    font-style: italic;
    color: var(--accent-orange);
    font-size: 27px;
    line-height: 33px;
  }
  .motto p { margin: 0; }
  .motto .values { word-spacing: 4px; }
</style>
</head>
<body>
<main class="card">
  <h1 class="creed-title">A 5-Point Creed</h1>
  <ol class="creed-list">
    <li>1. Be intentional to grow and learn new things each day.</li>
    <li>2. Honour God and others in everything you say and do.</li>
    <li>3. Act with integrity and uprightness in all matters.</li>
    <li>4. Prioritize serving and giving to others above yourself.</li>
    <li>5. Dream, pray, and expect for the impossible.</li>
  </ol>
  <section class="pledge">
    <h2 class="pledge-heading">Triple Crown &amp; 5-Point Creed Pledge:</h2>
    <p class="pledge-text">I commit to doing my best to live out the Triple Crown and 5-Point Creed each day.</p>
  </section>
  <div class="sign-field sign-signature">
    <div class="sign-line"></div>
    <span>Signature</span>
  </div>
  <div class="sign-field sign-date">
    <div class="sign-line"></div>
    <span>Date</span>
  </div>
  <footer class="motto">
    <p>Live every day with:</p>
    <p class="values">*&nbsp; Passion &nbsp;*&nbsp; Wonder &nbsp;*&nbsp; Playfulness &nbsp;*&nbsp; Gratitude &nbsp;*&nbsp;Love &nbsp;*</p>
  </footer>
</main>
</body>
</html>
```